Granite Ridge Holdings

I have a real estate investment business.

** I need editable vector files of the final design.

Industry/Entity Type

Real Estate

Contact Information for Business Card

I would like the card to be clear and direct with the company name and contact info. I would prefer not to have a design that is too busy (i.e., with excessive detail) in the business card.

Font styles to use
Sans Serif

Requirements
Must have
• My card must have the following information listed below:
• Company name: Grainite Ridge Holdings LLC
• My name: Daniel Vorsley
• Phone number: (555) 218-9067
• Email address: dtvorsley@mailbox-example.net
• Keywords: “Real Estate Investments”
Nice to have
• I would like to have a design that resembles the characteristics/uses of obsidian stone which resembles something related to strength and resilience. Perhaps something with sharp, sleek color transitions as well.

```html
<!DOCTYPE html>
<html lang="en">
<head>
<meta charset="UTF-8">
<title>Granite Ridge Holdings – Business Card</title>
<link href="https://fonts.googleapis.com/css2?family=Lato:wght@400&family=Roboto:wght@400;500&display=swap" rel="stylesheet">
<style>
  :root {
    --navy: #1f2272;
    --white: #ffffff;
    --ink: #3c3c46;
    --rule: #c9c9cf;
    --stage: #5b5b5e;
  }
  * { margin: 0; padding: 0; box-sizing: border-box; }
  html, body {
    width: 1200px; height: 802px; overflow: hidden;
    background: var(--stage);
  }
  .card {
    position: absolute;
    top: 274px;
    width: 443px; height: 265px;
    box-shadow: 2px 4px 8px rgba(0,0,0,.45);
    overflow: hidden;
  }
  .card-front { left: 136px; background: var(--white); }
  .card-back { left: 624px; background: var(--navy); }

  .brand {
    position: absolute; left: 0; top: 68px; width: 234px;
    text-align: center;
  }
  .brand-mark {
    display: block; margin: 0 auto 10px;
    width: 66px; height: 66px; border-radius: 50%;
    background: var(--navy);
  }
  .brand-name {
    font-family: "Roboto", sans-serif; font-weight: 500;
    font-size: 15.5px; letter-spacing: .5px; line-height: 1.2;
    color: var(--navy); text-transform: uppercase;
  }
  .divider {
    position: absolute; left: 234px; top: 89px;
    width: 1px; height: 85px; background: var(--rule);
  }
  .holder {
    position: absolute; left: 253px; top: 88px;
    font-family: "Roboto", sans-serif; font-weight: 500;
    font-size: 16.5px; color: var(--navy); text-transform: uppercase;
    letter-spacing: -.2px;
  }
  .contact {
    position: absolute; left: 253px; top: 142px;
    list-style: none;
    font-family: "Lato", sans-serif; font-size: 11.8px; color: var(--ink);
    line-height: 16.5px;
  }
  .contact li { display: flex; align-items: center; gap: 4px; white-space: nowrap; }
  .contact svg { width: 11px; height: 10px; fill: var(--navy); flex: none; }
  .keyword-band {
    position: absolute; left: 0; bottom: 0; width: 100%; height: 48px;
    background: var(--navy); color: var(--white);
    display: flex; align-items: center; justify-content: center;
    font-family: "Roboto", sans-serif; font-weight: 400; font-size: 12.5px;
    text-transform: uppercase;
  }
  .back-lockup {
    position: absolute; right: 62px; top: 101px;
    display: flex; align-items: center; gap: 10px;
  }
  .back-brand {
    font-family: "Roboto", sans-serif; font-weight: 500; font-size: 10px;
    letter-spacing: .6px; line-height: 1.3; text-align: right;
    color: var(--white); text-transform: uppercase;
  }
  .back-mark {
    flex: none;
    width: 50px; height: 50px; border-radius: 50%;
    background: var(--white);
  }
</style>
</head>
<body>
  <section class="card card-front">
    <div class="brand">
      <span class="brand-mark"></span>
      <p class="brand-name">Granite Ridge<br>Holdings</p>
    </div>
    <div class="divider"></div>
    <h1 class="holder">Daniel Vorsley</h1>
    <ul class="contact">
      <li>
        <svg viewBox="0 0 12 10" aria-hidden="true"><path d="M1 3.2C1 1.5 3 .8 6 .8s5 .7 5 2.4V4H8.6V3H3.4v1H1zM2.6 5h6.8l1.6 4.2H1z"/></svg>
        (555) 218-9067
      </li>
      <li>
        <svg viewBox="0 0 12 10" aria-hidden="true"><path d="M.5 1h11v8H.5zM1.5 2v.4L6 5.6l4.5-3.2V2L6 5.1z" fill-rule="evenodd"/></svg>
        dtvorsley@mailbox-example.net
      </li>
    </ul>
    <div class="keyword-band">Real Estate Investments</div>
  </section>

  <section class="card card-back">
    <div class="back-lockup">
      <p class="back-brand">Granite Ridge<br>Holdings</p>
      <span class="back-mark"></span>
    </div>
  </section>
</body>
</html>
```